Online Psychiatry business - Business Card

I need a business card design. The target audience is busy professionals of any field (this therapy appeals best to 24-35 year olds). It involves psychiatry by tele-medicine (or video-conference). Nothing on it should be a giveaway that it's about mental health. Professional design with silver or gold as the primary colors appeals to me. The card must be as simple and as uncluttered as possible. Some color and flowing design on the edge of the card appeals to me.
CrestLumaCareNet.com should probably appear in the center of the card and stand out, i.e. bold lettering, and easy to read, no cursive, but Ariel Black. Some where below this, should appear "Too Busy to Take Care of Yourself? Think again." Since this isn't office based, I don't think an office address is necessary and limits clutter.
Information that does need to appear is my name: Gerald Mewkinson, MD
General phone number: 618-472-9086. I'm hoping to get an 24-hour answering service soon so leave a little room for this. In addition I want to include two email addresses:
CrestLumaCareNet@mailvora.com and CrestLumaCare247@mailvora.com
Updates

I like the designs. I would like someone to put the website in bold in the center

 as most have been doing with a smaller font reminder nearby saying "No time" etc.
but I'd like to put my name down in the corner with the rest of the contact material.
Black print against a white or grey background appeals to me, with darker silver artwork near the sides (simple abstract, like wavy lines or something you can one up with that works. 
thanks

I ve tried to provide as much feedback as possible given my time limits, so if you have extra questions, please feel free to email. I tried to attach a file of a business card I really like but make be difficult to actually manufacture. I'm going to send you a link to the photo. The card has a pull tab. There is not much information on the outside. In fact, if you were to design the outside, I would just print : Too Busy to Take Care of Yourself? Think Again.

When you pull the tab the remaining information is on the bottom half of the card. Please don't use the color pink!!!!
http://www.printfolkgallery.net/2009/05/100-really-creative-business-cards/
It is the 39th photo on the list, about 2/3ds of the way down the page. It is titled: Ruvelinkiste

#7 and #16 have an appeal to me, except for the dot patterns
Hope this helps

I'm running out of time and energy. I 've been trying to give do down the list and give  individual feedback but I won't be able to do that anymore.

So if you have any specific questions, write me, and again thank you for all your effort!!

I know i received your files, including your zip files, Tolkra,

but Milos, did you send me the files including ZIP on project 5139624?
thanks

Target Market(s)

Working professionals and executive, attorneys, etc.

Industry/Entity Type

Business

Logo Text

Don't Have Time to Take Care of Yourself? Think Again.

Logo styles of interest
Pictorial/Combination Logo
Wordmark Logo
Font styles to use
Other font styles liked:
• Ariel Black appeals to me the most

Requirements
Must have
• Want to emphasize that the website must be obvious, easily found (The CrestLumaCareNet.com)
For that reason i'd like the card to be white, and minimal decoration on one or both sides just to add some style and color
Nice to have
• A Very uncluttered, elegant design, and something that makes it stick in your head-doesn't everyone want the last?
Should not have
• Nothing on the card that give it away that this is about psychiatry, such as brain or other symbol, but also nothing that gives it away as a medical business, such as a stethoscope or red cross or anything.

```html
<!DOCTYPE html>
<html lang="en">
<head>
<meta charset="utf-8">
<title>CrestLumaCareNet.com – Business Card</title>
<link rel="stylesheet" href="https://fonts.googleapis.com/css2?family=Archivo+Black&family=Arimo:wght@400;700&display=swap">
<style>
  :root {
    --silver-deep: #a7a5a3;
    --silver-mid: #d6d2cd;
    --cream: #f2ece6;
    --sky-deep: #79a7cb;
    --sky-glow: #d3eaf8;
    --ink: #000000;
    --ink-soft: #3a3a3a;
  }
  html, body {
    margin: 0;
    padding: 0;
    width: 1200px;
    height: 686px;
    overflow: hidden;
    background: #ffffff;
  }
  .card {
    position: relative;
    width: 1200px;
    height: 686px;
    overflow: hidden;
    font-family: "Arimo", Arial, sans-serif;
    color: var(--ink);
  }
  .card__art {
    position: absolute;
    inset: 0;
    width: 1200px;
    height: 686px;
  }
  .card__text {
    position: absolute;
    margin: 0;
    line-height: 1;
    white-space: nowrap;
  }
  .website {
    left: 262px;
    top: 190px;
    font-family: "Archivo Black", "Arial Black", sans-serif;
    font-size: 60px;
    letter-spacing: -2px;
  }
  .contact-name {
    right: 207px;
    top: 315px;
    font-weight: 700;
    font-size: 32px;
  }
  .contact-phone {
    right: 211px;
    top: 352px;
    font-size: 24px;
  }
  .contact-email {
    right: 275px;
    font-size: 24px;
    color: var(--ink-soft);
  }
  .contact-email--primary { top: 412px; }
  .contact-email--urgent { top: 446px; }
  .tagline-question {
    left: 46px;
    top: 562px;
    font-size: 26px;
    line-height: 41px;
    white-space: normal;
    width: 300px;
  }
  .tagline-answer {
    right: 45px;
    top: 604px;
    font-size: 28px;
  }
</style>
</head>
<body>
  <main class="card">
    <svg class="card__art" viewBox="0 0 1200 686" aria-hidden="true">
      <defs>
        <radialGradient id="sky" cx="1110" cy="250" r="520" gradientUnits="userSpaceOnUse">
          <stop offset="0" stop-color="var(--sky-glow)"/>
          <stop offset="0.35" stop-color="#8ec4e6"/>
          <stop offset="1" stop-color="var(--sky-deep)"/>
        </radialGradient>
        <linearGradient id="silver" x1="0" y1="0" x2="1185" y2="0" gradientUnits="userSpaceOnUse">
          <stop offset="0" stop-color="var(--silver-deep)"/>
          <stop offset="0.3" stop-color="var(--silver-mid)"/>
          <stop offset="0.6" stop-color="var(--cream)"/>
          <stop offset="1" stop-color="var(--cream)"/>
        </linearGradient>
      </defs>
      <rect class="sky-field" width="1200" height="686" fill="url(#sky)"/>
      <polygon class="arrow-panel" points="0,0 745,0 1185,340 720,686 0,686" fill="url(#silver)"/>
    </svg>

    <h1 class="card__text website">CrestLumaCareNet.com</h1>
    <p class="card__text contact-name">Gerald Mewkinson, MD</p>
    <p class="card__text contact-phone">618-472-9086</p>
    <p class="card__text contact-email contact-email--primary">CrestLumaCareNet@mailvora.com</p>
    <p class="card__text contact-email contact-email--urgent">CrestLumaCare247@mailvora.com</p>
    <p class="card__text tagline-question">Too Busy to Take Care of Yourself?</p>
    <p class="card__text tagline-answer">Think again.</p>
  </main>
</body>
</html>
```